Stationery Design Needed: Business Card, Letterhead, Folder Design

Logo files attached I plan on using the standard us folder size 9x12 as well as standard US business card and letter head. I am the owner of Meadowfall Restorative Spine Clinic, www.meadowfallspineclinic.example. I now have two locations, each with the same phone number and website. I enclosed my slogan and the information. I practice in an honest, ethical manor and place patients at a top priority. I want the designs to fit with my logo which symbolizes a blend of the symbol for ethical, honesty ( the peacock ) and the medusa ( medicine ) . I want to use the colors form my website blue, grey, silver to blend in and be cohesive and also match along the modern but natural colors along with blue and grey from the office. I want my cards and stationary to stand out

Target Market(s)

Lawyers, Surgeons, Primary Care Physicians Chiropractors

Industry/Entity Type

Business

Contact Information for Business Card

I want the cards and folders to stand out ...Bold colors I like the dark blue the best as I want this to be my signature color ...See below
I don t want too much white or too much aqua blue

Colors
3277b5

Requirements
Must have
• On Business cards... Must have logo, My name and practice, Two addresses, and my certifications from anesthesia and pain medicine .... web site easy to read for my target age audience 40 +
Nice to have
• slogan and other certifications
Should not have
• Confusing small to real letters ... so may need double sides but with all important on the front

```html
<!DOCTYPE html>
<html lang="en">
<head>
<meta charset="utf-8">
<title>Meadowfall Restorative Spine Clinic — Stationery Set</title>
<link rel="stylesheet" href="https://fonts.googleapis.com/css2?family=Montserrat:wght@600;700;800&family=Quicksand:wght@400;500;600;700&family=Arimo:wght@400;700&display=swap">
<style>
  :root {
    --board: #8b8b8b;
    --navy: #1e3564;
    --navy-ink: #1b2f5c;
    --accent: #2f5ea8;
    --paper: #ffffff;
    --text: #1a1a1a;
    --label: #ffffff;
    --shadow: rgba(0,0,0,0.45);
  }
  * { margin: 0; padding: 0; box-sizing: border-box; }
  html, body { width: 1200px; height: 1200px; overflow: hidden; }
  body { background: var(--board); position: relative; font-family: "Arimo", Arial, sans-serif; }

  .section-label {
    position: absolute; width: 400px; margin-left: -200px; text-align: center;
    font-family: "Arimo", Arial, sans-serif; font-weight: 700; font-size: 21px; color: var(--label);
  }

  .piece { position: absolute; box-shadow: 4px 4px 6px var(--shadow); overflow: hidden; }

  /* Letterhead */
  .letterhead { left: 11px; top: 72px; width: 582px; height: 770px; background: var(--paper); }
  .letterhead .brand-name {
    position: absolute; left: 32px; top: 178px; width: 190px;
    font-family: "Montserrat", sans-serif; font-weight: 700; font-size: 15px; line-height: 1.25;
    color: var(--navy-ink); text-transform: uppercase;
  }
  .letterhead .contact {
    position: absolute; right: 26px; top: 48px; text-align: right;
    font-family: "Quicksand", sans-serif; font-weight: 500; font-size: 10.5px; color: var(--navy-ink);
    line-height: 21px;
  }
  .letterhead .contact b { font-weight: 700; }
  .letterhead .contact .web { font-weight: 600; letter-spacing: 0.3px; }
  .letterhead .contact .addr { font-weight: 600; line-height: 17px; margin-top: 4px; }
  .letter { position: absolute; left: 44px; top: 314px; width: 530px; font-size: 12.8px; color: var(--text); }
  .letter .salutation { font-weight: 700; letter-spacing: 0.3px; }
  .letter .body { margin-top: 24px; text-align: justify; line-height: 17.5px; letter-spacing: 0.4px; }
  .letter .signoff { margin-top: 46px; line-height: 19px; }
  .letter .signoff b { letter-spacing: 0.3px; }

  /* Folder */
  .folder { left: 608px; top: 72px; width: 581px; height: 770px; background: var(--navy); color: #fff; text-align: center; }
  .folder .brand-circle {
    position: absolute; left: 50%; top: 150px; width: 240px; height: 240px; margin-left: -120px;
    border: 10px solid #fff; border-radius: 50%;
  }
  .folder .brand-name {
    position: absolute; left: 0; right: 0; top: 540px;
    font-family: "Montserrat", sans-serif; font-weight: 700; color: #fff; text-transform: uppercase;
  }
  .folder .brand-name .line-1 { display: block; font-size: 72px; line-height: 80px; letter-spacing: 1px; }
  .folder .brand-name .line-2 { display: block; font-size: 23px; line-height: 30px; letter-spacing: 0.5px; margin-top: 8px; }
  .folder .web {
    position: absolute; left: 0; right: 0; top: 724px;
    font-family: "Quicksand", sans-serif; font-weight: 700; font-size: 19px; letter-spacing: 2.4px;
  }

  /* Business card front */
  .card-front { left: 97px; top: 871px; width: 411px; height: 246px; background: var(--navy); color: #fff; text-align: center; }
  .card-front .brand-name {
    position: absolute; left: 0; right: 0; top: 70px;
    font-family: "Montserrat", sans-serif; font-weight: 700; font-size: 18px; line-height: 24px; text-transform: uppercase;
  }
  .card-front .cert-title {
    position: absolute; left: 0; right: 0; top: 183px;
    font-family: "Quicksand", sans-serif; font-weight: 600; font-size: 10px;
  }
  .card-front .cert-rule { position: absolute; left: 154px; width: 101px; top: 198px; height: 1.5px; background: #fff; }
  .card-front .cert-list {
    position: absolute; left: 0; right: 0; top: 205px;
    font-family: "Quicksand", sans-serif; font-weight: 500; font-size: 10px; line-height: 14px; color: #d6dcea; letter-spacing: 0.3px;
  }

  /* Business card back */
  .card-back { left: 693px; top: 871px; width: 411px; height: 246px; background: var(--paper); }
  .card-back .brand-name {
    position: absolute; left: 14px; top: 118px; width: 180px;
    font-family: "Montserrat", sans-serif; font-weight: 700; font-size: 15px; line-height: 20px; color: var(--navy-ink); text-transform: uppercase;
  }
  .card-back .details {
    position: absolute; right: 26px; top: 33px; text-align: right;
    font-family: "Quicksand", sans-serif; color: var(--navy-ink);
  }
  .card-back .name { font-weight: 600; font-size: 14.5px; line-height: 16px; }
  .card-back .addr-main { margin-top: 16px; font-weight: 600; font-size: 11.5px; line-height: 16px; color: #111; }
  .card-back .addr-second { margin-top: 14px; font-weight: 500; font-size: 11.5px; line-height: 16px; color: #333; }
  .card-back .phones { margin-top: 14px; font-weight: 500; font-size: 12px; line-height: 19px; color: #333; }
  .card-back .phones b { color: var(--navy-ink); font-weight: 700; }
  .card-back .band {
    position: absolute; left: 0; right: 0; bottom: 0; height: 33px; background: var(--navy);
    font-family: "Quicksand", sans-serif; font-weight: 600; font-size: 11.5px; color: #fff; text-align: center; line-height: 33px; letter-spacing: 0.3px;
  }
</style>
</head>
<body>

  <div class="section-label" style="left:302px; top:36px;">Letterhead A4</div>
  <div class="section-label" style="left:898px; top:36px;">Folder 9 X 12</div>

  <section class="piece letterhead" aria-label="Letterhead">
    <div class="brand-name">Meadowfall Restorative Spine Clinic</div>
    <div class="contact">
      <div><b>PH :</b> 555-014-2290</div>
      <div><b>F :</b> 555-014-2291</div>
      <div class="web">www.meadowfallspineclinic.example</div>
      <div class="addr">4180 Alder Park Ave Brookvale,<br>N.J. 07999</div>
    </div>
    <div class="letter">
      <p class="salutation">Dear Mr.Daniel Hartwell</p>
      <p class="body">Logo files attached I plan on using the standard us folder size 9x12 as well as standard US business card and letter head. I am the owner of Meadowfall Restorative Spine Clinic, www.meadowfallspineclinic.example. I now have two locations, each with the same phone number and website. I enclosed my slogan and the information. I practice in an honest, ethical manor and place patients at a top priority. I want the designs to fit with my logo which symbolizes a blend of the symbol for ethical, honesty ( the peacock ) and the medusa ( medicine ) . I want to use the colors form my website blue, grey, silver to blend in and be cohesive and also match along the modern but natural colors along with blue and grey from the office. I want my cards and stationary to stand out<br>Thank you.</p>
      <p class="signoff"><b>Jordan Pike</b><br>Graphic Designer</p>
    </div>
  </section>

  <section class="piece folder" aria-label="Presentation folder">
    <div class="brand-circle"></div>
    <div class="brand-name">
      <span class="line-1">Meadowfall</span>
      <span class="line-2">Restorative Spine Clinic</span>
    </div>
    <div class="web">www.meadowfallspineclinic.example</div>
  </section>

  <section class="piece card-front" aria-label="Business card front">
    <div class="brand-name">Meadowfall<br>Restorative Spine Clinic</div>
    <div class="cert-title">Board Certifications</div>
    <div class="cert-rule"></div>
    <div class="cert-list">
      Certified by the Allied Council of Pain Medicine<br>
      Certified by the Allied Council of Anesthesiology
    </div>
  </section>

  <section class="piece card-back" aria-label="Business card back">
    <div class="brand-name">Meadowfall<br>Restorative<br>Spine Clinic</div>
    <div class="details">
      <div class="name">Daniel R. Hartwell,<br>D.O.</div>
      <div class="addr-main">4180 Alder Park Ave<br>Brookvale, N.J. 07999</div>
      <div class="addr-second">820 Route 9 West, Suite 110<br>Lindenfield, N.J., 07988-1100</div>
      <div class="phones"><b>Ph :</b> 555-014-2290<br><b>Fax :</b> 555-014-2291</div>
    </div>
    <div class="band">www.meadowfallspineclinic.example</div>
  </section>

  <div class="section-label" style="left:302px; top:1132px;">Front Side</div>
  <div class="section-label" style="left:898px; top:1132px;">Back Side</div>

</body>
</html>
```